I need a flyer made , the flyer can be one page or two pages or three pages . I will be posting this on Instagram and social media platforms. I am a luxury home builder , I am looking to hire a construction project manager . Below are some examples and ideas what can be on the flyer

We’re looking for a construction project manager who’s passionate about building luxury homes at the highest standards
We’re hiring construction project manager
* Experience 5+ years in residential project management with a strong portfolio of completed homes.
* location : Bergen County NJ
* excellent leadership skills, leads teams with confidence and clarity
* communicates seamlessly with architects , engineers, designers and clients
*knows how to manage budgets and timelines without compromising quality
*solves problems with a positive solution first mindset
* pays attention to every detail because in luxury the small things are the big things

Apply now , link in bio or DM to connect.

My logo is attached, my web site www.ridgelanebuilders.com
My style is modern but still warm and inviting. I like a clean classy look .
Updates

Please don’t add any images of chairs or people to the flyer , I do not want people on my flyer. Do not add standard images of offices and houses , we are luxury builders , we build homes over 2 million dollars. Keep a classy , simple modern look . High end .

You can add a white hard hat with my logo on it for a image , this is a suggestion does not have to be on my flyer ,

```html
<!DOCTYPE html>
<html lang="en">
<head>
<meta charset="utf-8">
<title>Ridgelane Builders – Hiring Flyer</title>
<link rel="stylesheet" href="https://fonts.googleapis.com/css2?family=Montserrat:wght@400;500;600;700;800;900&display=swap">
<style>
  :root {
    --stage: #e8e5e1;
    --ink: #0b0b0c;
    --ink-soft: #1a1a1c;
    --orange: #f7a21b;
    --white: #ffffff;
    --panel-top: #f4f3f6;
    --panel-bottom: #dcdae0;
    --text-dark: #141414;
  }
  * { margin: 0; padding: 0; box-sizing: border-box; }
  html, body {
    width: 1200px; height: 800px; overflow: hidden;
    background: var(--stage);
    font-family: "Montserrat", Arial, sans-serif;
  }
  .flyer {
    position: absolute; left: 330px; top: 18px;
    width: 540px; height: 764px;
    background: radial-gradient(ellipse at 75% 20%, #1c1c1f 0%, var(--ink) 60%);
    overflow: hidden;
  }
  .hero-visual {
    position: absolute; right: 20px; top: 22px;
    width: 230px; height: 190px;
    border-radius: 12px;
    background: radial-gradient(ellipse at 55% 50%, #f2a52a 0%, #6e6e70 40%, #262628 75%, transparent 100%);
    opacity: .9;
  }
  .brand {
    position: absolute; left: 38px; top: 112px;
    color: var(--white);
    font-weight: 400; font-size: 27px; letter-spacing: 3px;
    line-height: 1.15;
    display: flex; align-items: center; gap: 10px;
  }
  .brand-dot { width: 9px; height: 9px; border-radius: 50%; background: var(--white); }
  .headline { position: absolute; left: 38px; top: 165px; width: 310px; }
  .headline-lead { color: var(--orange); font-weight: 700; font-size: 15px; letter-spacing: .3px; }
  .headline-role { color: var(--white); font-weight: 800; font-size: 15px; letter-spacing: .3px; margin-top: 2px; }
  .headline-sub { color: var(--orange); font-weight: 600; font-size: 13px; line-height: 1.35; margin-top: 5px; }
  .details-panel {
    position: absolute; left: 34px; top: 276px;
    width: 472px; height: 398px;
    border-radius: 22px;
    background: linear-gradient(160deg, var(--panel-top) 0%, var(--panel-bottom) 100%);
  }
  .hiring-badge { position: absolute; left: 14px; top: 20px; }
  .role-title {
    position: absolute; left: 196px; top: 26px;
    color: var(--text-dark); font-weight: 900; font-size: 19px; line-height: 1.15;
  }
  .requirements {
    position: absolute; left: 22px; top: 104px; width: 420px;
    list-style: none;
  }
  .requirements::before {
    content: ""; position: absolute; left: 5px; top: 8px; bottom: 6px;
    border-left: 2px dotted var(--orange);
  }
  .requirement {
    position: relative; padding-left: 24px; margin-bottom: 11px;
    color: var(--text-dark); font-weight: 500; font-size: 12.5px; line-height: 1.4;
  }
  .requirement::before {
    content: ""; position: absolute; left: 0; top: 3px;
    width: 12px; height: 12px; border-radius: 50%;
    border: 2px solid var(--orange);
    box-shadow: inset 0 0 0 2px var(--panel-top), inset 0 0 0 6px var(--orange);
  }
  .requirement strong { font-weight: 800; }
  .apply-pill {
    position: absolute; left: 38px; top: 696px;
    background: var(--orange); color: var(--text-dark);
    font-weight: 900; font-size: 14px; letter-spacing: .3px;
    padding: 6px 18px; border-radius: 20px;
  }
  .connect {
    position: absolute; left: 186px; top: 694px;
    color: var(--white); font-weight: 900; font-size: 14px; letter-spacing: .3px;
  }
  .website {
    position: absolute; left: 186px; top: 716px;
    color: var(--white); font-weight: 500; font-size: 13px; letter-spacing: .3px;
  }
</style>
</head>
<body>
  <main class="flyer">
    <div class="hero-visual" role="img" aria-label="Orange hard hat with blueprints and a construction crane scene"></div>

    <div class="brand"><span class="brand-dot"></span>RIDGELANE BUILDERS</div>

    <header class="headline">
      <p class="headline-lead">WE'RE LOOKING FOR A</p>
      <p class="headline-role">CONSTRUCTION PROJECT MANAGER</p>
      <p class="headline-sub">who's passionate about building luxury homes at the highest standards</p>
    </header>

    <section class="details-panel">
      <svg class="hiring-badge" width="170" height="74" viewBox="0 0 170 74" aria-label="We're hiring">
        <polygon points="60,6 168,6 150,68 42,68" fill="var(--orange)"/>
        <polygon points="4,14 112,8 104,38 0,44" fill="var(--ink-soft)"/>
        <text x="14" y="35" fill="#fff" font-family="Montserrat, sans-serif" font-weight="900" font-size="19">WE'RE</text>
        <text x="60" y="62" fill="var(--text-dark)" font-family="Montserrat, sans-serif" font-weight="900" font-size="26">HIRING</text>
      </svg>
      <h2 class="role-title">CONSTRUCTION<br>PROJECT MANAGER</h2>

      <ul class="requirements">
        <li class="requirement">Experience 5+ years in residential project management with a strong portfolio of completed homes.</li>
        <li class="requirement"><strong>LOCATION :</strong> Bergen County NJ</li>
        <li class="requirement">Excellent leadership skills, leads teams with confidence and clarity</li>
        <li class="requirement">Communicates seamlessly with architects, engineers, designers and clients</li>
        <li class="requirement">Knows how to manage budgets &amp; timelines without compromising quality</li>
        <li class="requirement">Solves problems with a positive solution first mindset</li>
        <li class="requirement">Pays attention to every detail because in luxury the small things are the big things</li>
      </ul>
    </section>

    <div class="apply-pill">APPLY NOW</div>
    <p class="connect">LINK IN BIO OR DM TO CONNECT.</p>
    <p class="website">www.ridgelanebuilders.com</p>
  </main>
</body>
</html>
```